Toy Company Needs a Web Site For a New Toy

We need a web site for a new toy called "Zippa Loop Trike". The bike is a plastic, non motorized ride on toy for kids ages 1.5 - 5 years of age. The bike is being launched in three colors, red, blue and pink, though we may include a black option too.

For the web site we want something bold and colorful that communicates fun, therefore NO dull colors like black or grey. Nothing too cluttered. We want the site to attract the attention of kids but also give the parents a sense of confidence in our professionalism as a trustworthy toy company. The home page should focus on the bike, with different views of the bike and a small write-up on some of its key features. We would also like the home page to have a video of the bike in play. A obvious link to the shopping basket must be present as well. The site must include a shopping basket and ordering system.

Attached is a screenshot of a site that has the colourfulness and playfulness that we are looking for. Please have a look.

The bike images attached are renderings from the CAD software, actual high res photos will be used when the site is developed.

The product logo is attached and MUST be used on the site. It must be BOLD and can be incorporated into the actual website design.

The site pages are:
Home
Gallery
Buy
Contact

Competitors:
www.brambleplay.example
www.quorvaride.example
I do not like either of their sites.

We only have one product at this time, so the site is to be focused on that product, not a whole catalog of products. It is really a single product with the ability to purchase.
Updates

Project Deadline Extended
Reason: I am extending this competition in order to give me more time to review each design and provide the feedback that the designers deserve.

Target Market(s)

Parents, children ages 1.5 - 5.

Industry/Entity Type

It Company

Colors
0555a3
eb1f27
9bcb3c
faed22
f78f20
f37022
e34197
a6459a
6b449b

Requirements
Must have
• Please use the logo attached, but feel free to use different colors.
Should not have
• Dull colors like black and grey

```html
<!DOCTYPE html>
<html lang="en">
<head>
<meta charset="utf-8">
<title>Zippa Loop Trike</title>
<link rel="stylesheet" href="https://fonts.googleapis.com/css2?family=Arimo:wght@400;700&family=Source+Sans+3:wght@400;600;700&display=swap">
<style>
  :root {
    --sky: #e4f2fa;
    --title-blue: #2aa3d9;
    --nav-top: #28c0ee;
    --nav-bottom: #0a9bd3;
    --nav-edge: #0b86b8;
    --home-yellow: #ffe21a;
    --cart-top: #d9e64a;
    --cart-bottom: #b9cb1e;
    --orange-top: #fbc02a;
    --orange-bottom: #ea940c;
    --red-top: #ee3a32;
    --red-bottom: #cf1b17;
    --price-red: #e2201c;
    --body-text: #6a6a6a;
    --dark-text: #333333;
    --footer-text: #4a4a4a;
    --white: #ffffff;
    --grass: #b7d868;
    --swatch-red: #e8212a;
    --swatch-blue: #2ea4dc;
    --swatch-pink: #ee4fb8;
  }
  * { box-sizing: border-box; margin: 0; padding: 0; }
  html, body { width: 981px; height: 1200px; overflow: hidden; }
  body {
    position: relative;
    background: linear-gradient(180deg, #d8edf6 0px, var(--sky) 150px, var(--sky) 968px);
    font-family: "Arimo", Arial, sans-serif;
    color: var(--body-text);
  }
  .abs { position: absolute; }

  /* header */
  .brand { left: 125px; top: 46px; display: flex; align-items: center; gap: 10px; }
  .brand-dot { width: 44px; height: 44px; border-radius: 50%; background: var(--title-blue); }
  .brand-name { font-family: "Source Sans 3", sans-serif; font-weight: 700; font-size: 24px; color: var(--title-blue); }

  .toggle-group { top: 46px; height: 24px; display: flex; border: 1px solid #c3cdd2; border-radius: 12px; background: linear-gradient(#fafcfd, #e4eaed); overflow: hidden; }
  .toggle-group span { width: 25px; line-height: 22px; text-align: center; font-size: 10px; color: #777; border-right: 1px solid #c9d1d5; }
  .toggle-group span:last-child { border-right: 0; }
  .toggle-group .active { color: var(--dark-text); background: #fff; }
  .currency { left: 694px; }
  .language { left: 777px; }

  .search { left: 648px; top: 79px; width: 210px; height: 24px; border: 1px solid #e8c98e; border-radius: 4px; background: linear-gradient(#fff, #fdf1d8); display: flex; }
  .search-label { flex: 1; padding-left: 10px; line-height: 22px; font-family: "Source Sans 3", sans-serif; font-size: 11px; color: #6f6f6f; }
  .search-btn { width: 24px; background: linear-gradient(var(--orange-top), var(--orange-bottom)); display: flex; align-items: center; justify-content: center; }

  /* nav */
  .nav { left: 125px; top: 134px; width: 733px; height: 32px; border-radius: 5px; border: 1px solid var(--nav-edge); background: linear-gradient(var(--nav-top), var(--nav-bottom)); }
  .nav-link { top: 0; line-height: 30px; font-family: "Source Sans 3", sans-serif; font-weight: 600; font-size: 11px; color: var(--white); }
  .nav-link.current { color: var(--home-yellow); }
  .nav-sep { top: 6px; width: 1px; height: 20px; background: rgba(255,255,255,.25); }
  .cart { left: 520px; top: 4px; width: 186px; height: 23px; border-radius: 3px 0 0 3px; background: linear-gradient(var(--cart-top), var(--cart-bottom)); display: flex; justify-content: space-between; padding: 0 8px; line-height: 23px; font-family: "Source Sans 3", sans-serif; font-size: 10.5px; color: #3c4a10; }
  .cart-icon { left: 708px; top: 4px; width: 22px; height: 23px; border-radius: 0 3px 3px 0; background: linear-gradient(var(--cart-top), var(--cart-bottom)); display: flex; align-items: center; justify-content: center; }

  /* hero */
  .hero { left: 125px; top: 178px; width: 733px; height: 258px; border-radius: 3px; overflow: hidden; }
  .hero-photo { position: absolute; inset: 0; background: linear-gradient(100deg, #7d7468 0%, #a39583 30%, #d7b59c 48%, #b8434f 70%, #9e2a36 100%); }
  .hero-caption { position: absolute; left: 79px; background: var(--white); font-family: "Arimo", Arial, sans-serif; font-size: 16px; padding: 0 6px; line-height: 27px; }
  .hero-caption.c1 { top: 82px; color: var(--title-blue); }
  .hero-caption.c1 em { font-style: normal; color: #f49a1c; }
  .hero-caption.c2 { top: 115px; color: var(--price-red); }
  .hero-caption.c3 { top: 148px; color: var(--title-blue); }

  .btn { display: inline-block; height: 22px; line-height: 22px; border-radius: 11px; text-align: center; font-family: "Arimo", Arial, sans-serif; font-weight: 700; font-size: 9.5px; color: var(--white); }
  .btn-orange { background: linear-gradient(var(--orange-top), var(--orange-bottom)); box-shadow: 0 1px 0 #c97908; }
  .btn-red { background: linear-gradient(var(--red-top), var(--red-bottom)); box-shadow: 0 1px 0 #a31410; }
  .hero .btn { position: absolute; left: 79px; top: 210px; width: 78px; }

  /* product */
  .product-photo { left: 152px; top: 464px; width: 216px; height: 208px; border-radius: 40px; background: radial-gradient(circle at 50% 45%, #f7c6de 0%, #eea4c9 45%, rgba(238,164,201,0) 72%); }
  .section-title { font-family: "Source Sans 3", sans-serif; font-weight: 400; font-size: 16px; color: var(--title-blue); }
  .product-title { left: 436px; top: 484px; }
  .copy { font-size: 9.6px; line-height: 14px; color: var(--body-text); }
  .product-copy { left: 436px; top: 510px; width: 384px; }
  .price { left: 435px; top: 571px; font-family: "Source Sans 3", sans-serif; font-size: 15px; color: var(--title-blue); }
  .price strong { font-size: 20px; font-weight: 700; color: var(--price-red); }
  .colors { left: 436px; top: 600px; display: flex; align-items: center; gap: 6px; font-size: 9.6px; font-weight: 700; color: var(--dark-text); }
  .swatches { display: flex; gap: 1px; }
  .swatches i { width: 11px; height: 11px; display: block; }
  .product-actions { left: 436px; top: 626px; display: flex; gap: 7px; }
  .product-actions .btn { width: 81px; }

  /* about & video */
  .about-title { left: 138px; top: 706px; }
  .about-copy { left: 138px; top: 734px; width: 312px; }
  .about-copy p + p { margin-top: 14px; }
  .about-btn { left: 139px; top: 880px; width: 78px; }
  .video-title { left: 469px; top: 705px; }
  .video-frame { left: 470px; top: 732px; width: 376px; height: 194px; border: 1px solid #c9d3d8; border-radius: 4px; background: var(--white); padding: 5px; box-shadow: 0 1px 3px rgba(0,0,0,.12); }
  .video-screen { position: relative; width: 100%; height: 100%; overflow: hidden; background: linear-gradient(180deg, #5f8e2c 0%, #78a83a 50%, #6a9b30 100%); }
  .video-bar { position: absolute; left: 0; right: 0; top: 0; height: 19px; background: rgba(40,50,20,.7); line-height: 19px; padding-left: 12px; font-size: 7.5px; color: var(--white); }
  .video-play { position: absolute; left: 164px; top: 64px; }
  .video-progress { position: absolute; left: 10px; right: 10px; bottom: 7px; display: flex; align-items: center; gap: 10px; }
  .video-track { flex: 1; height: 2px; background: var(--white); position: relative; }
  .video-track::before { content: ""; position: absolute; left: 0; top: -2px; width: 6px; height: 6px; border-radius: 50%; background: #222; }

  /* footer */
  .footer { left: 0; top: 968px; width: 981px; height: 232px; background: var(--white); box-shadow: 0 -2px 4px rgba(120,160,180,.15); }
  .meadow { position: absolute; left: 0; bottom: 0; width: 981px; height: 96px; background: linear-gradient(180deg, rgba(183,216,104,0) 0%, #d7eaa8 45%, var(--grass) 100%); }
  .footer-col { top: 41px; }
  .footer-col h3 { font-family: "Source Sans 3", sans-serif; font-weight: 400; font-size: 12.5px; color: var(--dark-text); margin-bottom: 9px; }
  .footer-col ul { list-style: none; padding-left: 9px; }
  .footer-col li { position: relative; font-family: "Source Sans 3", sans-serif; font-size: 8.5px; line-height: 18.7px; text-transform: uppercase; color: var(--footer-text); }
  .footer-col li::before { content: "›"; position: absolute; left: -9px; top: -1px; font-size: 11px; color: var(--dark-text); }
  .to-top { left: 934px; top: 1133px; width: 34px; height: 34px; border-radius: 4px; background: linear-gradient(#fbc66a, #f5a12a); display: flex; align-items: center; justify-content: center; }
</style>
</head>
<body>

<header>
  <div class="abs brand">
    <span class="brand-dot"></span>
    <span class="brand-name">Zippa Loop Trike</span>
  </div>

  <div class="abs toggle-group currency"><span>€</span><span>£</span><span class="active">$</span></div>
  <div class="abs toggle-group language"><span class="active">EN</span><span>DE</span></div>

  <div class="abs search">
    <span class="search-label">Search</span>
    <span class="search-btn">
      <svg width="12" height="12" viewBox="0 0 12 12"><circle cx="5" cy="5" r="3.4" fill="none" stroke="#6b3d05" stroke-width="1.6"/><line x1="7.5" y1="7.5" x2="11" y2="11" stroke="#6b3d05" stroke-width="2" stroke-linecap="round"/></svg>
    </span>
  </div>

  <nav class="abs nav">
    <span class="abs nav-link current" style="left:21px">Home</span>
    <span class="abs nav-sep" style="left:63px"></span>
    <span class="abs nav-link" style="left:77px">Gallery</span>
    <span class="abs nav-sep" style="left:126px"></span>
    <span class="abs nav-link" style="left:144px">Buy</span>
    <span class="abs nav-sep" style="left:177px"></span>
    <span class="abs nav-link" style="left:196px">Contact</span>
    <div class="abs cart"><span>Shopping Cart</span><span>0 item(s) - $0.00</span></div>
    <div class="abs cart-icon">
      <svg width="14" height="12" viewBox="0 0 14 12"><path d="M0.5 1h2.3l1.8 7h7l1.6-5H4" fill="none" stroke="#3c4a10" stroke-width="1.2"/><circle cx="5.5" cy="10.5" r="1" fill="#3c4a10"/><circle cx="10.5" cy="10.5" r="1" fill="#3c4a10"/></svg>
    </div>
  </nav>
</header>

<main>
  <section class="abs hero">
    <div class="hero-photo" role="img" aria-label="Photo of a young child in a red checked shirt leaning over colourful toy blocks"></div>
    <div class="hero-caption c1">Lorem ipsum dolor <em>sit amet</em></div>
    <div class="hero-caption c2">Consectetur adipisicing elit, sed</div>
    <div class="hero-caption c3">Do eiusmod tempor</div>
    <span class="btn btn-orange">Read more</span>
  </section>

  <div class="abs product-photo" role="img" aria-label="Photo of the pink ride-on trike"></div>
  <h2 class="abs section-title product-title">Super New Bike This Year</h2>
  <p class="abs copy product-copy">Lorem ipsum dolor sit amet, consectetur adipisicing elit, sed do eiusmod tempor incididunt ut labore et dolore magna aliqua. Ut enim ad minim veniamLorem ipsum dolor sit ametLorem ipsum dolor sit ametLorem ipsum dolor sit ametLorem ipsum dolor sit ametLorem ipsum dolor sit amet,</p>
  <div class="abs price">Price: <strong>$230</strong></div>
  <div class="abs colors">Color selection:
    <span class="swatches"><i style="background:var(--swatch-red)"></i><i style="background:var(--swatch-blue)"></i><i style="background:var(--swatch-pink)"></i></span>
  </div>
  <div class="abs product-actions">
    <span class="btn btn-red">Add to cart</span>
    <span class="btn btn-orange">Details</span>
  </div>

  <h2 class="abs section-title about-title">About Us</h2>
  <div class="abs copy about-copy">
    <p>Lorem ipsum dolor sit amet, consectetur adipisicing elit, sed do eiusmod tempor incididunt ut labore et dolore magna aliqua.</p>
    <p>cillum dolore eu fugiat nulla pariatur. Excepteur sint occaecat cupidatat non proident, sunt in culpa qui officia deserunt mollit anim id est laborumLorem ipsum dolor sit amet, consectetur adipisicing elit, sed do eiusmod tempor incididunt ut labore et dolore magna aliqua. Ut enim ad minim veniamLorem ipsum dolor sit ametLorem ipsum dolor sit ametLorem</p>
  </div>
  <span class="abs btn btn-orange about-btn">Read more</span>

  <h2 class="abs section-title video-title">Promotional Video</h2>
  <div class="abs video-frame">
    <div class="video-screen" role="img" aria-label="Video still of a child in a helmet riding a balance bike on grass">
      <div class="video-bar">Lorem ipsum dolor sit amet, consectetur adipisicing elit</div>
      <svg class="video-play" width="36" height="36" viewBox="0 0 36 36" aria-hidden="true"><circle cx="18" cy="18" r="16" fill="rgba(60,60,60,.55)" stroke="#fff" stroke-width="2"/><path d="M14 10l12 8-12 8z" fill="#fff"/></svg>
      <div class="video-progress">
        <svg width="8" height="8" viewBox="0 0 8 8" aria-hidden="true"><path d="M1 0l7 4-7 4z" fill="#fff"/></svg>
        <div class="video-track"></div>
      </div>
    </div>
  </div>
</main>

<footer class="abs footer">
  <div class="meadow" role="img" aria-label="Illustrated meadow with grass, flowers and trees"></div>

  <div class="abs footer-col" style="left:130px">
    <h3>Information</h3>
    <ul><li>About Us</li><li>Delivery Information</li><li>Privacy Policy</li><li>Terms &amp; Conditions</li></ul>
  </div>
  <div class="abs footer-col" style="left:313px">
    <h3>Customer Service</h3>
    <ul><li>Contact Us</li><li>Returns</li><li>Site Map</li></ul>
  </div>
  <div class="abs footer-col" style="left:495px">
    <h3>Extras</h3>
    <ul><li>Brands</li><li>Gift Vouchers</li><li>Affiliates</li><li>Specials</li></ul>
  </div>
  <div class="abs footer-col" style="left:678px">
    <h3>My Account</h3>
    <ul><li>My Account</li><li>Order History</li><li>Wish List</li><li>Newsletter</li></ul>
  </div>
</footer>

<div class="abs to-top">
  <svg width="18" height="12" viewBox="0 0 18 12" aria-hidden="true"><path d="M2 10l7-7 7 7" fill="none" stroke="#fff" stroke-width="2.5"/></svg>
</div>

</body>
</html>
```